Kestrel Fuelworks Brochure Updates

We are looking to freshen up our equipment brochures and have them all made into one printable book as well (additional cover page to the existing brochures) and update the look on the brochures.
***NOTE***
Just do one brochure update and once we pick the design we like we will update the other 4 outside of this project with one on one award to the winning designer

Target Market(s)

Oilfield Field staff and executives

Industry/Entity Type

Oil And Gas

Requirements
Must have
• Must have the information currently on the brochures. we just want to clean it up with a more corporate feel and square the design up a bit.
Nice to have
• Clean, easy to read, and good picture sizes

```html
<!DOCTYPE html>
<html lang="en">
<head>
<meta charset="utf-8">
<title>LED Mobile Lighting – Kestrel Fuelworks</title>
<link rel="stylesheet" href="https://fonts.googleapis.com/css2?family=Montserrat:wght@300;400;600;700&display=swap">
<style>
  :root {
    --backdrop: #e9e6e1;
    --night: #07080b;
    --snow: #c9ccd2;
    --navy: #1a3a78;
    --lime: #b4bd2c;
    --paper: #ffffff;
    --ink: #3a3d44;
    --white: #ffffff;
  }
  * { margin: 0; padding: 0; box-sizing: border-box; }
  html, body {
    width: 1200px; height: 803px; overflow: hidden;
    background: var(--backdrop);
    font-family: "Montserrat", sans-serif;
  }
  .stage {
    width: 1200px; height: 803px;
    display: flex; align-items: center; justify-content: center;
  }
  .cover {
    position: relative;
    width: 530px; height: 750px;
    background: var(--paper);
    overflow: hidden;
    box-shadow: 0 6px 24px rgba(0,0,0,.18);
  }
  .cover__photo {
    position: absolute; left: 0; top: 0;
    width: 100%; height: 372px;
    background:
      radial-gradient(ellipse 60% 40% at 55% 85%, rgba(235,238,243,.95), rgba(200,204,212,.6) 55%, transparent 80%),
      linear-gradient(180deg, var(--night) 0%, #0d0f14 50%, #3b3f48 72%, var(--snow) 100%);
  }
  .cover__tagline {
    position: absolute; left: 40px; top: 52px;
    width: 240px;
    color: var(--white);
    font-size: 9.5px; font-weight: 400;
    letter-spacing: .06em; line-height: 1.55;
    text-transform: uppercase;
  }
  .cover__inset {
    position: absolute; right: 36px; top: 22px;
    width: 176px; height: 176px;
    border: 2px solid var(--lime);
    border-radius: 0 34px 0 34px;
    background:
      radial-gradient(ellipse 70% 35% at 55% 90%, #eef0f4, #b9bdc6 60%, transparent 85%),
      linear-gradient(180deg, #050608 0%, #10131a 55%, #cdd0d6 100%);
  }
  .cover__divider {
    position: absolute; left: 0; top: 360px;
    width: 100%; height: 30px;
  }
  .cover__band {
    position: absolute; left: 0; top: 374px;
    width: 100%; height: 256px;
    background: var(--navy);
  }
  .cover__title {
    position: absolute; left: 78px; top: 470px;
    line-height: 1.08;
  }
  .cover__title-light {
    display: block;
    color: var(--white);
    font-size: 40px; font-weight: 300;
  }
  .cover__title-bold {
    display: block;
    color: var(--lime);
    font-size: 40px; font-weight: 700;
  }
  .cover__web {
    position: absolute; right: 40px; top: 652px;
    color: var(--ink);
    font-size: 10px; font-weight: 400;
  }
  .cover__brand {
    position: absolute; left: 36px; bottom: 30px;
    display: flex; align-items: center; gap: 8px;
    color: var(--lime);
    font-size: 15px; font-weight: 700;
  }
  .cover__brand-dot {
    width: 16px; height: 16px; border-radius: 50%;
    background: var(--navy);
  }
</style>
</head>
<body>
  <main class="stage">
    <article class="cover">
      <div class="cover__photo" role="img" aria-label="Night photo of a mobile LED light tower illuminating a snowy oilfield lease site with equipment"></div>
      <p class="cover__tagline">Implementing technologies that reduce costs, improve efficiency, and decrease environmental impact</p>
      <div class="cover__inset" role="img" aria-label="Close-up night photo of a raised LED light tower over snow"></div>

      <div class="cover__band"></div>
      <svg class="cover__divider" viewBox="0 0 530 30" preserveAspectRatio="none" aria-hidden="true">
        <polygon points="0,22 530,4 530,14 0,30" fill="#1a3a78"/>
        <polygon points="0,18 530,0 530,5 0,23" fill="#b4bd2c"/>
      </svg>

      <h1 class="cover__title">
        <span class="cover__title-light">LED Mobile</span>
        <span class="cover__title-bold">Lighting</span>
      </h1>

      <p class="cover__web">www.kestrelfuelworks.ca</p>
      <div class="cover__brand">
        <span class="cover__brand-dot"></span>
        <span>Kestrel Fuelworks</span>
      </div>
    </article>
  </main>
</body>
</html>
```